Heritage Hollow Business Cards

Require a business card design. <br/><br/>Needs to include logo (either round or long version) plus these details:<br/>Maya Torvel<br/>Heritage Hollow<br/>maya@quonbrook.com.au<br/>02 6481 7390<br/>PO Box Glenwarra NSW 2913<br/>www.heritagehollow.com.au<br/><br/>I need in an editable format so that I can create for multiple staff members. <br/><br/>

Target Market(s)

We are an online store selling renovation products to home owners are builders. Looking for a classic classy design.

Industry/Entity Type

Home And Garden

Contact Information for Business Card

Maya Torvel
Heritage Hollow
maya@quonbrook.com.au
02 6481 7390
PO Box Glenwarra NSW 2913
www.heritagehollow.com.au

Colors

Designer to choose colors to be used in the design.

Requirements
Must have
• Must include Logo.

```html
<!DOCTYPE html>
<html lang="en">
<head>
<meta charset="utf-8">
<title>Heritage Hollow Business Card</title>
<link rel="stylesheet" href="https://fonts.googleapis.com/css2?family=Aleo:wght@300;400&display=swap">
<style>
  :root {
    --backdrop: #3a3a3a;
    --brand-red: #ef393d;
    --pattern-red: #f0585a;
    --paper: #ffffff;
  }
  * { margin: 0; padding: 0; box-sizing: border-box; }
  html, body { width: 1200px; height: 1000px; overflow: hidden; }
  body {
    position: relative;
    background: var(--backdrop);
    font-family: "Aleo", Georgia, serif;
  }
  .card {
    position: absolute;
    top: 20px;
    width: 548px;
    height: 958px;
    overflow: hidden;
  }
  .card-front { left: 31px; background: var(--brand-red); }
  .card-back { left: 618px; background: var(--paper); }

  .brand-pattern {
    position: absolute;
    inset: 0;
    background: linear-gradient(180deg, var(--brand-red), #f04a4c 50%, var(--brand-red));
  }
  .front-mark {
    position: absolute;
    left: 102px;
    top: 318px;
    width: 344px;
    height: 344px;
    border: 3px solid var(--paper);
    border-radius: 50%;
    background: var(--brand-red);
    display: flex;
    align-items: center;
    justify-content: center;
  }
  .front-mark .brand-name {
    color: var(--paper);
    font-size: 40px;
    font-weight: 400;
    line-height: 1.05;
    text-align: center;
  }

  .name-band {
    position: absolute;
    left: 0; top: 0;
    width: 100%;
    height: 180px;
    background: var(--brand-red);
    border-radius: 0 0 88px 88px;
    color: var(--paper);
  }
  .person-name {
    position: absolute;
    right: 172px;
    top: 72px;
    font-size: 42px;
    font-weight: 400;
    line-height: 1;
    text-decoration: underline;
    text-decoration-thickness: 2px;
    text-underline-offset: 5px;
  }
  .person-role {
    position: absolute;
    right: 172px;
    top: 120px;
    font-size: 20px;
    font-weight: 400;
  }

  .back-mark {
    position: absolute;
    left: 96px;
    top: 226px;
    width: 354px;
    height: 354px;
    border: 3px solid var(--brand-red);
    border-radius: 50%;
    display: flex;
    align-items: center;
    justify-content: center;
  }
  .back-mark .brand-name {
    color: var(--brand-red);
    font-size: 42px;
    font-weight: 400;
    line-height: 1.05;
    text-align: center;
  }

  .contact-panel {
    position: absolute;
    left: 0; bottom: 0;
    width: 100%;
    height: 338px;
    background: var(--brand-red);
    border-radius: 88px 88px 0 0;
    color: var(--paper);
  }
  .contact-list {
    list-style: none;
    position: absolute;
    left: 72px;
    top: 66px;
    font-size: 20px;
    font-weight: 400;
    line-height: 1.35;
  }
  .contact-list li {
    position: relative;
    padding-left: 42px;
    margin-bottom: 11px;
  }
  .contact-list li::before {
    content: "";
    position: absolute;
    left: 0;
    top: 6px;
    width: 16px;
    height: 16px;
    border-radius: 50%;
    background: var(--paper);
    box-shadow: 0 0 0 2px var(--brand-red) inset, 0 0 0 1.5px var(--paper);
  }
</style>
</head>
<body>
  <section class="card card-front">
    <div class="brand-pattern" role="img" aria-label="Faint repeated brand pattern across the card face"></div>
    <div class="front-mark">
      <p class="brand-name">Heritage<br>Hollow</p>
    </div>
  </section>

  <section class="card card-back">
    <header class="name-band">
      <h1 class="person-name">Maya Torvel</h1>
      <p class="person-role">Director</p>
    </header>

    <div class="back-mark">
      <p class="brand-name">Heritage<br>Hollow</p>
    </div>

    <footer class="contact-panel">
      <ul class="contact-list">
        <li>Heritage Hollow<br>P O Box Glenwarra NSW 2913.</li>
        <li>02-6481-7390</li>
        <li>www.heritagehollow.com.au</li>
        <li>maya@quonbrook.com.au</li>
      </ul>
    </footer>
  </section>
</body>
</html>
```